Real Estate Investment Company needs postcard design

We need a postcard design for a Real Estate Investment company named 'Brightpath Homestead Partners, LLC'. We are a residential redevelopment company who specializes in buying distressed homes at a significant discount, and renovate and resell them to retail home buyers and landlords. Our service is to give home owners an option to contact us if they want to sell their home. We would like to see designs that use our logo with a modern and friendly feel. These post cards will be going out to clients who are in stressful situations (foreclosure, estate sales, etc.) and would like them to feel comfortable and safe when receiving this postcard. The final design should communicate stress free and fast solution for their situation.
Real Estate

```html
<!DOCTYPE html>
<html lang="en">
<head>
<meta charset="utf-8">
<title>Brightpath Homestead Partners – Postcard</title>
<link href="https://fonts.googleapis.com/css2?family=Montserrat:wght@300;400;800&family=Source+Sans+3:ital,wght@0,400;0,600;0,700;1,400&family=Roboto:wght@700&display=swap" rel="stylesheet">
<style>
  :root{
    --blue:#1f7fc9;
    --blue-deep:#155fa3;
    --blue-light:#5aa7e0;
    --ink:#111417;
    --text:#222;
    --paper:#ffffff;
    --stage:#e8e9eb;
    --slot:#eeeeee;
  }
  *{margin:0;padding:0;box-sizing:border-box}
  html,body{width:1200px;height:1200px;overflow:hidden}
  body{background:var(--stage);position:relative;font-family:"Source Sans 3",sans-serif;color:var(--text)}
  .card{position:absolute;left:225px;width:750px;height:575px;background:var(--paper);overflow:hidden;box-shadow:0 6px 18px rgba(0,0,0,.18)}
  .card--front{top:20px}
  .card--back{top:605px}
  .card svg.shapes{position:absolute;inset:0;width:750px;height:575px}
  .brand{position:absolute;display:flex;align-items:center;gap:8px;color:var(--blue);font-weight:700;font-family:"Source Sans 3",sans-serif}
  .brand__mark{width:14px;height:14px;background:var(--blue);flex:none}
  .card--front .brand{left:44px;top:42px;font-size:27px;line-height:1.05;width:300px}
  .card--back .brand{left:428px;top:60px;font-size:17px;line-height:1.05;width:150px}
  .front__title{position:absolute;left:40px;top:178px;font-family:"Montserrat",sans-serif;font-weight:800;font-size:38px;letter-spacing:1px;color:var(--ink);line-height:1}
  .front__subtitle{position:absolute;left:40px;top:222px;font-family:"Montserrat",sans-serif;font-weight:400;font-size:20px;color:var(--blue);letter-spacing:.5px}
  .front__body{position:absolute;left:40px;top:268px;width:335px;font-size:17.5px;line-height:22.5px;text-align:justify;color:var(--ink)}
  .section-label{position:absolute;display:flex;align-items:center;gap:8px;color:var(--blue);font-weight:600}
  .section-label::after{content:"";display:block;height:3px;background:var(--blue)}
  .front__contact{left:40px;top:372px;font-size:30px}
  .front__contact::after{width:76px}
  .front__phone{position:absolute;left:40px;top:412px;font-family:"Roboto",sans-serif;font-weight:700;font-size:36px;color:var(--ink)}
  .back__heading{position:absolute;left:34px;top:278px;font-size:19px;font-weight:600;color:var(--ink)}
  .back__heading span,.back__visit span{color:var(--blue)}
  .back__body{position:absolute;left:31px;top:307px;width:266px;font-size:12.6px;line-height:15.6px;font-style:italic;text-align:justify;color:var(--ink)}
  .back__visit{position:absolute;left:34px;top:444px;display:flex;align-items:center;gap:6px;font-size:19px;font-weight:600;color:var(--ink)}
  .back__visit::after{content:"";display:block;width:116px;height:2px;background:var(--blue)}
  .back__web{position:absolute;left:33px;top:468px;display:flex;align-items:center;gap:8px;font-size:19px;color:var(--ink);white-space:nowrap}
  .back__address{position:absolute;left:32px;top:518px;font-size:15.5px;line-height:18px;color:#fff;font-weight:600;display:flex;gap:6px}
  .slot{position:absolute;background:var(--slot)}
  .slot--stamp{left:586px;top:44px;width:110px;height:110px}
  .slot--address{left:418px;top:286px;width:280px;height:132px}
</style>
</head>
<body>

<section class="card card--front">
  <svg class="shapes" viewBox="0 0 750 575">
    <defs>
      <linearGradient id="towerTone" x1="0" y1="0" x2="1" y2="1">
        <stop offset="0" stop-color="#cfe3f5"/><stop offset=".5" stop-color="#4f93d2"/><stop offset="1" stop-color="#1a5fa4"/>
      </linearGradient>
      <linearGradient id="dealTone" x1="0" y1="0" x2="1" y2="1">
        <stop offset="0" stop-color="#4a5563"/><stop offset=".5" stop-color="#b79b86"/><stop offset="1" stop-color="#9cc9d8"/>
      </linearGradient>
      <linearGradient id="bandTone" x1="0" y1="0" x2="1" y2="0">
        <stop offset="0" stop-color="#2a8ad4"/><stop offset="1" stop-color="#166db8"/>
      </linearGradient>
    </defs>
    <polygon points="0,117 400,144 400,162 0,123" fill="var(--blue)"/>
    <polygon points="345,0 392,0 470,362 452,372" fill="var(--ink)"/>
    <polygon points="358,0 400,0 476,362 462,366" fill="var(--blue)"/>
    <polygon role="img" aria-label="Photo of a glass office tower seen from below" points="398,0 750,0 750,360 480,362" fill="url(#towerTone)"/>
    <polygon points="0,562 420,457 700,382 750,362 750,372 700,392 420,465 0,570" fill="var(--ink)"/>
    <polygon points="0,570 420,465 700,392 750,372 750,575 0,575" fill="url(#bandTone)"/>
    <polygon points="405,385 555,305 705,385 705,505 555,585 405,505" fill="var(--ink)"/>
    <polygon points="414,390 555,315 696,390 696,500 555,575 414,500" fill="#fff"/>
    <polygon role="img" aria-label="Photo of a handshake over a desk with a small model house" points="424,395 555,325 686,395 686,495 555,565 424,495" fill="url(#dealTone)"/>
  </svg>

  <div class="brand"><span class="brand__mark"></span>Brightpath Homestead</div>
  <h1 class="front__title">BRIGHTPATH</h1>
  <p class="front__subtitle">HOMESTEAD PARTNERS, LLC</p>
  <p class="front__body">Lorem Ipsum is simply dummy text of the printing and typesetting industry. Lorem Ipsum has been the industry's standard dummy text ever since the 1500s,</p>
  <p class="section-label front__contact">Contact Us</p>
  <p class="front__phone">(480) 555-0172</p>
</section>

<section class="card card--back">
  <svg class="shapes" viewBox="0 0 750 575">
    <defs>
      <linearGradient id="skyTone" x1="0" y1="0" x2="0" y2="1">
        <stop offset="0" stop-color="#2a78c6"/><stop offset=".55" stop-color="#a9cdec"/><stop offset="1" stop-color="#dbe9f5"/>
      </linearGradient>
      <linearGradient id="coupleTone" x1="0" y1="0" x2="1" y2="1">
        <stop offset="0" stop-color="#e7e3dc"/><stop offset=".5" stop-color="#c89a80"/><stop offset="1" stop-color="#3fa5cf"/>
      </linearGradient>
      <linearGradient id="panelTone" x1="0" y1="0" x2="1" y2="0">
        <stop offset="0" stop-color="#ffffff"/><stop offset="1" stop-color="#e4e4e4"/>
      </linearGradient>
    </defs>
    <polygon role="img" aria-label="Photo of a businessman on a ladder reaching toward cloud lettering in a blue sky" points="0,0 305,0 340,95 335,200 0,272" fill="url(#skyTone)"/>
    <polygon points="0,272 335,200 330,262 305,510 0,510" fill="url(#panelTone)"/>
    <polygon points="0,266 300,208 300,214 0,274" fill="var(--ink)"/>
    <polygon points="322,262 330,262 305,510 297,510" fill="var(--blue)"/>
    <polygon points="340,262 362,262 345,455 262,575 240,575 322,455" fill="var(--ink)"/>
    <polygon points="240,110 335,55 430,110 430,215 335,272 240,215" fill="var(--ink)"/>
    <polygon role="img" aria-label="Photo of a smiling couple holding up the keys to their new house" points="250,115 335,66 420,115 420,210 335,260 250,210" fill="url(#coupleTone)"/>
    <polygon points="0,508 305,508 258,575 0,575" fill="var(--blue)"/>
  </svg>

  <div class="brand"><span class="brand__mark"></span>Brightpath Homestead</div>
  <div class="slot slot--stamp"></div>
  <div class="slot slot--address"></div>

  <h2 class="back__heading">About <span>Us</span></h2>
  <p class="back__body">Lorem Ipsum is simply dummy text of the printing and typesetting industry. Lorem Ipsum has been the industry's standard dummy text ever since the 1500s, when an unknown printer took a galley of type and scrambled it to make a type specimen book. It has survived not only five centuries, but also the leap into electronic typesetting, remaining essentially unchanged.</p>
  <p class="back__visit">Visit <span>Us</span></p>
  <p class="back__web">
    <svg width="13" height="13" viewBox="0 0 14 14" aria-hidden="true"><circle cx="7" cy="7" r="6" fill="none" stroke="var(--blue)" stroke-width="1.6"/><path d="M1 7h12M7 1c-3 3-3 9 0 12M7 1c3 3 3 9 0 12" fill="none" stroke="var(--blue)" stroke-width="1.2"/></svg>
    www.bphomestead.com
  </p>
  <div class="back__address">
    <svg width="10" height="14" viewBox="0 0 10 14" aria-hidden="true"><path d="M5 0a5 5 0 0 1 5 5c0 3.5-5 9-5 9S0 8.5 0 5a5 5 0 0 1 5-5z" fill="#fff"/><circle cx="5" cy="5" r="2" fill="var(--blue)"/></svg>
    <p>Harlow Ridge Services<br>PO Box 41127 Tempe, AZ 85281</p>
  </div>
</section>

</body>
</html>
```